Amber Tides: Lantern Tales from Seven Winters by the Northern Sea and Other Small Wonders

Good day! I am excited to work again with you, amazing designers! This time I am looking for the cover design of my book.
Dimensions 6” x 9”
The book name is as my name project. I love simplicity, but yet that is impactful. I love colours, I don't have a specific colour in mind, but I like the mustard colour as the one in the logo of my company. I am open to ideas! I have attached some cover samples that I like so that it gives a better idea of what I have on mind.
I am looking for something that looks professional, yet, not super serious, that it's approachable to people. Something that calls their attention at first glance.
I am working with my editor and my interior designer as well to finalize this part of the book. I will be working with the person that I select for the book design to finalize it.
About the book, here a passage of an unedited version of the introduction for guidance :
My intention is to take you on a journey to help you to understand what is going on in your mind so that you get out from anything that is holding you back in your life. My intention is to guide you to start fully living and experiencing a life that your mind even have yet conceived. To experience a life where you live fearless and without suffering. Living your life where you are the navigator and the creator of how you are experiencing it and you are living in a world of possibilities where there are no limitations.
For it, we will start to understand more about the mind and about the brain. I am not a neuroscientist and neither I consider my self an expert in the workings of the brain, what I know is the result of my fascination about our brain. This curiosity and the part of me that likes to understand how things work took me to read, research and learn about how our brain works and how its intrinsic mechanisms are subconsciously influencing and limiting us. I encourage you to stay on this part, it can be a bit technical, but understanding how it works will empower you not to allow your mind to dictate the way you approach your life and to live on autopilot.
We will continue to describe how you have been programmed throughout your life, putting you inside a box limited by your subconscious beliefs and ideas about the world. In this part, we will also discuss what ego is, how it is subconsciously limiting you and how the ways of when ego manifests itself are limiting you and making you suffer. Now that you know how you have been enclosed in your mind for all your life, we will move to discuss how you can get out of it. You will learn how to master your emotions to eliminate your suffering and not allow them to control the direction of your life and use them as a mechanism to get out from your programed mind. We continue to discuss how to leverage the power of your mind and harness your power of choice. Finally, I invite you to see yourself as a holistic being so that you start truly living and take control over the direction of your life, by nourishing and taking care of all those aspects of you utilizing their wisdom and synergy to achieve higher connection within yourself, your soul and live your life in a higher level of consciousness with peace, flow, love and purpose.

```html
<!DOCTYPE html>
<html lang="en">
<head>
<meta charset="utf-8">
<title>Amber Tides — Book Cover</title>
<link href="https://fonts.googleapis.com/css2?family=Open+Sans:wght@600;700&family=Yellowtail&display=swap" rel="stylesheet">
<style>
  :root {
    --page-bg: #e6dcc0;
    --mustard: #ecbf45;
    --title-shadow: #2a1d10;
    --sky-top: #1f2a66;
    --sky-mid: #5a5a8e;
    --cloud: #b9aec4;
    --horizon: #e9a552;
    --sand: #b8581c;
    --sand-dark: #4e2410;
  }
  * { margin: 0; padding: 0; box-sizing: border-box; }
  html, body {
    width: 1200px; height: 800px; overflow: hidden;
    background: var(--page-bg);
  }
  .canvas {
    position: relative; width: 1200px; height: 800px;
    display: flex; align-items: center; justify-content: center;
  }
  .book-cover {
    position: relative; width: 460px; height: 690px; overflow: hidden;
    box-shadow: 0 6px 18px rgba(60, 45, 20, 0.35);
  }
  .cover-photo {
    position: absolute; inset: 0;
    background: linear-gradient(180deg,
      var(--sky-top) 0%,
      var(--sky-mid) 30%,
      var(--cloud) 52%,
      var(--horizon) 68%,
      var(--sand) 82%,
      var(--sand-dark) 100%);
  }
  .subtitle-band {
    position: absolute; top: 0; left: 0; right: 0; height: 66px;
    background: rgba(20, 28, 80, 0.35);
  }
  .subtitle {
    position: absolute; top: 17px; left: 20px; right: 20px;
    font-family: "Open Sans", sans-serif; font-weight: 600;
    font-size: 14px; line-height: 1.4; text-align: center;
    color: var(--mustard);
    text-shadow: 0 1px 2px rgba(0,0,0,0.45);
  }
  .title {
    position: absolute; top: 110px; left: 0; right: 0;
    font-family: "Yellowtail", cursive; font-weight: 400;
    font-size: 74px; line-height: 1; text-align: center;
    white-space: nowrap;
    color: var(--mustard);
    text-shadow: 3px 4px 0 var(--title-shadow);
    transform: rotate(-4deg);
  }
  .title-swash {
    position: absolute; top: 196px; left: 250px;
  }
  .author {
    position: absolute; bottom: 24px; left: 0; right: 0;
    font-family: "Open Sans", sans-serif; font-weight: 700;
    font-size: 26px; text-align: center; letter-spacing: 0.5px;
    color: var(--mustard);
    text-shadow: 1px 2px 2px rgba(40, 15, 0, 0.6);
  }
</style>
</head>
<body>
<main class="canvas">
  <article class="book-cover">
    <div class="cover-photo" role="img" aria-label="Photograph of a beach at sunset with a cloudy blue sky, waves and golden sand"></div>
    <div class="subtitle-band"></div>
    <p class="subtitle">Lantern Tales from Seven Winters by the Northern Sea and Other Small Wonders</p>
    <h1 class="title">Amber Tides</h1>
    <svg class="title-swash" width="180" height="40" viewBox="0 0 180 40" aria-hidden="true">
      <path d="M6 32 C 60 24, 110 14, 172 6" fill="none" stroke="#2a1d10" stroke-width="4" stroke-linecap="round" transform="translate(3 3)"/>
      <path d="M6 32 C 60 24, 110 14, 172 6" fill="none" stroke="#ecbf45" stroke-width="4" stroke-linecap="round"/>
    </svg>
    <p class="author">Author Name</p>
  </article>
</main>
</body>
</html>
```